regPersonal Trainer Flyer Design

Reason: I have been very busy with other work and would like to extend the deadline to offer designers the chance to edit and improve designs with my help. Thank you for all the designs that have been sent so far.

```html
<!DOCTYPE html>
<html lang="en">
<head>
<meta charset="utf-8">
<title>Fitness Training Flyer</title>
<link href="https://fonts.googleapis.com/css2?family=PT+Sans:wght@400;700&family=Open+Sans:wght@400;700;800&family=Gochi+Hand&display=swap" rel="stylesheet">
<style>
  :root {
    --sky-top: #2f6fc4;
    --sky-mid: #8fb2e3;
    --sky-light: #dfe8f6;
    --band-blue: #1f5fb8;
    --band-deep: #17509f;
    --ink: #1d1410;
    --ink-soft: #2b2420;
    --white: #ffffff;
    --sun: #f2c01e;
    --sun-deep: #e0a90c;
    --photo-warm: #b79a86;
    --photo-cool: #9aa6b6;
    --ghost: rgba(255,255,255,0.45);
  }
  * { margin: 0; padding: 0; box-sizing: border-box; }
  html, body { width: 1200px; height: 851px; overflow: hidden; }
  body { font-family: "PT Sans", "Open Sans", sans-serif; }

  .flyer {
    position: relative;
    width: 1200px; height: 851px; overflow: hidden;
    background: linear-gradient(180deg, var(--sky-top) 0%, var(--sky-mid) 28%, var(--sky-light) 55%, #c7d7ee 78%, var(--sky-mid) 90%);
  }

  .backdrop-photo {
    position: absolute; left: 540px; top: 150px; width: 520px; height: 620px;
    background: radial-gradient(ellipse at 50% 40%, rgba(255,255,255,0.55) 0%, rgba(220,228,240,0.35) 45%, rgba(200,214,236,0) 75%);
  }

  .headline { position: absolute; left: 118px; top: 40px; color: var(--ink); }
  .headline-main {
    font-family: "Open Sans", sans-serif; font-weight: 800;
    font-size: 118px; line-height: 1; letter-spacing: -2px;
    color: var(--white);
    text-shadow: 0 2px 6px rgba(0,0,0,0.25);
  }
  .headline-sub {
    font-family: "Open Sans", sans-serif; font-weight: 800;
    font-size: 62px; line-height: 1; letter-spacing: 15px;
    margin-top: 22px; color: var(--ink);
  }
  .headline-tag {
    font-family: "PT Sans", sans-serif; font-weight: 400;
    font-size: 46px; line-height: 1; margin-top: 10px; color: var(--ink);
  }

  .pain-points {
    position: absolute; left: 770px; top: 80px; list-style: none;
    font-family: "Open Sans", sans-serif; font-weight: 700;
    font-size: 24px; line-height: 36px; color: var(--ink-soft);
  }
  .pain-points li { position: relative; padding-left: 28px; }
  .pain-points li::before {
    content: ""; position: absolute; left: 4px; top: 11px;
    border-left: 10px solid var(--white);
    border-top: 7px solid transparent; border-bottom: 7px solid transparent;
  }

  .offer-burst { position: absolute; left: 30px; top: 312px; width: 280px; height: 280px; }
  .offer-text {
    position: absolute; left: 62px; top: 392px; width: 200px;
    transform: rotate(-32deg); text-align: center;
    font-family: "Gochi Hand", cursive; color: var(--ink); line-height: 0.95;
  }
  .offer-text .small { font-size: 36px; display: block; }
  .offer-text .big { font-size: 50px; display: block; }

  .photo-circle {
    position: absolute; border-radius: 50%;
    border: 10px solid var(--white);
    box-shadow: 0 4px 14px rgba(0,0,0,0.25);
  }
  .photo-session {
    left: 232px; top: 340px; width: 468px; height: 468px;
    background: radial-gradient(circle at 40% 35%, #e9e2dc 0%, var(--photo-warm) 55%, #6d5d55 100%);
  }
  .photo-pads {
    left: 28px; top: 532px; width: 290px; height: 290px;
    background: radial-gradient(circle at 50% 45%, #d9c9bf 0%, var(--photo-warm) 50%, #5a4a44 100%);
  }

  .trainer-portrait {
    position: absolute; left: 800px; top: 342px; width: 212px; height: 230px;
    background: radial-gradient(ellipse at 50% 45%, #d6b8a2 0%, var(--photo-cool) 60%, rgba(200,214,236,0) 100%);
  }

  .trainer-id { position: absolute; left: 796px; top: 654px; font-family: "PT Sans", sans-serif; color: var(--ink); }
  .trainer-name { font-weight: 700; font-size: 44px; line-height: 1; }
  .trainer-role { font-weight: 400; font-size: 29px; letter-spacing: 1.5px; margin-top: 8px; color: var(--ink-soft); }

  .contact-band {
    position: absolute; left: 0; top: 768px; width: 1200px; height: 83px;
    background: linear-gradient(180deg, var(--band-blue), var(--band-deep));
  }
  .contact-list {
    position: absolute; left: 604px; top: 786px; display: flex; gap: 22px; align-items: center;
    font-family: "Open Sans", sans-serif; font-weight: 700; font-size: 23px; color: var(--white);
  }
  .contact-item { display: flex; align-items: center; gap: 10px; }
  .contact-icon { width: 38px; height: 38px; }
</style>
</head>
<body>
<main class="flyer">
  <div class="backdrop-photo" role="img" aria-label="Faded photo of a smiling woman exercising in a gym"></div>

  <header class="headline">
    <h1 class="headline-main">FITNESS</h1>
    <p class="headline-sub">TRAINING</p>
    <p class="headline-tag">can be at your home</p>
  </header>

  <ul class="pain-points">
    <li>Lacking motivation?</li>
    <li>Not achieving your goals?</li>
    <li>Need help?</li>
    <li>Bored of the gym?</li>
    <li>You're never too old</li>
    <li>I can help improve your<br>health and well-being</li>
  </ul>

  <div class="photo-circle photo-pads" role="img" aria-label="Photo of a woman punching training pads"></div>
  <div class="photo-circle photo-session" role="img" aria-label="Photo of a woman doing a squat while the trainer coaches her"></div>

  <svg class="offer-burst" viewBox="0 0 280 280" aria-hidden="true">
    <defs>
      <radialGradient id="sunFill" cx="50%" cy="50%" r="50%">
        <stop offset="0%" stop-color="#ffd84a"/>
        <stop offset="100%" stop-color="#f2b81a"/>
      </radialGradient>
    </defs>
    <polygon fill="url(#sunFill)" stroke="#e0a90c" stroke-width="1"
      points="140,4 152,36 174,8 178,42 206,20 202,54 234,40 222,72 256,66 236,94 270,96 244,118 276,130 246,144 274,162 242,170 264,196 230,198 246,228 212,222 220,256 188,242 186,274 160,252 148,276 134,250 116,272 110,240 86,262 88,228 58,242 68,210 34,216 52,186 18,180 44,158 10,144 42,132 12,110 46,102 24,74 58,76 46,44 78,56 74,22 104,40 110,8 128,36"/>
  </svg>
  <div class="offer-text">
    <span class="small">One</span>
    <span class="big">FREE</span>
    <span class="small">Session</span>
  </div>

  <div class="trainer-portrait" role="img" aria-label="Head and shoulders photo of the personal trainer"></div>

  <div class="trainer-id">
    <p class="trainer-name">Sam Hollis</p>
    <p class="trainer-role">Personal Trainer</p>
  </div>

  <footer class="contact-band"></footer>
  <div class="contact-list">
    <div class="contact-item">
      <svg class="contact-icon" viewBox="0 0 38 38" aria-hidden="true">
        <circle cx="19" cy="19" r="18" fill="#f2c01e"/>
        <path d="M13 10 h5 l2 6 -3 2 c1 3 3 5 6 6 l2-3 6 2 v5 c0 1-1 2-2 2 C18 30 8 20 8 12 c0-1 1-2 2-2z" fill="#ffffff" transform="translate(1 -1) scale(0.92)"/>
      </svg>
      <span>07700900461</span>
    </div>
    <div class="contact-item">
      <svg class="contact-icon" viewBox="0 0 38 38" aria-hidden="true">
        <circle cx="19" cy="19" r="18" fill="#f2c01e"/>
        <rect x="9" y="12" width="20" height="14" rx="1.5" fill="#ffffff"/>
        <path d="M9.5 12.5 L19 20 L28.5 12.5" fill="none" stroke="#f2c01e" stroke-width="2"/>
      </svg>
      <span>samhollis@mailbox.co.uk</span>
    </div>
  </div>
</main>
</body>
</html>
```